Thought Harbor Tri-Fold Brochure - Recovering From Alzheimer's

Design a brochure a brochure for Thought Harbor. www.thoughtharbor.org. We help people with Alzheimer's, or who have had a Traumatic Brain Injury, Concussion or Stroke stop their cognitive decline, and actually reverse decline and improve their cognitive abilities. We use an individualized approach, utilizing extensive lab work and developing a roadmap that includes diet, supplementation, theraputic devices all guided by a Memory Coach. I would like to see a design with pictures of people similar to the demographic on the website. Also incorporate some of the colors from my logo. We offer hope to people who consistently hear, "There is nothing we can do. Alzheimer's is a fatal disease." NOT TRUE! We see people's lives change every day!!!!

Target Market(s)

People who ARE or know someone suffering from cognitive decline, Alzheimer's, Traumatic Brain Injury, Concussion or Stroke.

Industry/Entity Type

Health and wellbeing -- Treating Alzheimer's.

Font styles to use
Other font styles liked:
• Calibri or I think it's called Lota

Colors
0054AA
0677BA
7BADD7
CADEEF
E8F1F8
0094D4
00A9DD
6FCCEA
C7EBF8
E9F6FB
00AB8E
00BBA5
67D7C9
C6EFE9
E9F9F6

Requirements
Must have
• Easily read material (think older eyes) and people between the ages of 40-70. Needs to have a professional feel but not clinical. Create trust and a feeling of caring and hope.
Nice to have
• Please check out my website: www.thoughtharbor.org for content and feel.
Should not have
• Youthful people exercising OR highly stereotypical ageist photos or info.

```html
<!DOCTYPE html>
<html lang="en">
<head>
<meta charset="utf-8">
<title>Thought Harbor Tri-Fold Brochure</title>
<link rel="stylesheet" href="https://fonts.googleapis.com/css2?family=Playfair+Display:ital,wght@0,600;0,700;1,600&family=Montserrat:wght@500;700&family=Roboto:wght@400;500&display=swap">
<style>
:root{
  --stage:#3a3a3a;
  --paper:#ffffff;
  --paper-grey:#eeeeee;
  --blue:#0677ba;
  --blue-deep:#0054aa;
  --blue-soft:#7badd7;
  --blue-pale:#cadeef;
  --green:#1a8f2a;
  --green-soft:#b9dfc3;
  --ink:#1d1d1d;
  --white:#ffffff;
}
*{box-sizing:border-box;margin:0;padding:0}
html,body{width:785px;height:1200px;overflow:hidden;background:var(--stage)}
.spread{position:absolute;left:22px;width:740px;height:572px;overflow:hidden;background:var(--paper)}
.spread--outside{top:18px}
.spread--inside{top:610px}
.spread-art{position:absolute;inset:0}
.panel{position:absolute;top:0;width:246.67px;height:572px}
.panel--left{left:0}
.panel--middle{left:246.67px}
.panel--right{left:493.33px}
.fold{position:absolute;top:0;width:1px;height:572px;background:rgba(0,0,0,.08)}
.serif{font-family:"Playfair Display",Georgia,serif}
.sans{font-family:"Roboto",Arial,sans-serif}
.geo{font-family:"Montserrat",Arial,sans-serif}
.abs{position:absolute}
.heading{font-family:"Playfair Display",Georgia,serif;font-weight:700;color:var(--blue);line-height:1.1}
.rule{position:absolute;height:1px;background:var(--blue)}
.body-copy{font-family:"Roboto",Arial,sans-serif;color:var(--ink);font-size:9px;line-height:1.35;text-align:justify}
.ticks{list-style:none;font-family:"Roboto",Arial,sans-serif;color:var(--ink)}
.ticks li{position:relative;padding-left:16px}
.ticks li::before{content:"";position:absolute;left:0;top:3px;width:9px;height:9px;border:1.2px solid var(--blue);border-radius:50%}
.ticks li::after{content:"";position:absolute;left:3px;top:5.5px;width:3px;height:2px;border-left:1.2px solid var(--blue);border-bottom:1.2px solid var(--blue);transform:rotate(-45deg)}
.quote{font-family:"Playfair Display",Georgia,serif;font-style:italic;font-weight:600;color:var(--white);font-size:14px;line-height:1.35}
.brand-name{font-family:"Playfair Display",Georgia,serif;font-weight:700;color:var(--blue-deep);text-transform:uppercase;letter-spacing:.5px}
.pill{position:absolute;background:var(--white);border-radius:14px;color:var(--blue-deep);font-family:"Montserrat",Arial,sans-serif;font-weight:700;display:flex;align-items:center;justify-content:center;gap:6px}
.contact-line{font-family:"Montserrat",Arial,sans-serif;color:var(--white);font-size:11px;text-align:center}
.banner{position:absolute;background:var(--green);color:var(--white);font-family:"Montserrat",Arial,sans-serif;font-weight:700;font-size:14px;padding:4px 12px;letter-spacing:.3px}
.services{list-style:none;font-family:"Montserrat",Arial,sans-serif;font-weight:700;color:var(--ink);font-size:11.5px;line-height:1.75;text-transform:uppercase}
.services li{position:relative;padding-left:18px}
.services li::before{content:"";position:absolute;left:0;top:5px;width:10px;height:10px;border:1.2px solid var(--blue);border-radius:50%}
</style>
</head>
<body>

<!-- Outside spread -->
<section class="spread spread--outside">
  <svg class="spread-art" width="740" height="572" viewBox="0 0 740 572">
    <rect x="246.67" y="0" width="246.66" height="572" fill="var(--paper-grey)"/>
    <path d="M0,400 C60,432 150,442 200,402 C240,370 260,330 300,310 C330,296 350,292 380,292 L500,292 C560,300 610,334 740,322 L740,572 L0,572 Z" fill="var(--blue)"/>
    <path d="M40,412 C110,432 160,424 200,392 C240,360 260,320 300,300 C330,286 350,282 380,282 L520,282" fill="none" stroke="var(--green)" stroke-width="7"/>
    <circle cx="120" cy="300" r="100" fill="none" stroke="var(--green-soft)" stroke-width="4"/>
    <circle cx="120" cy="300" r="93" fill="#b48a4a" role="img" aria-label="Photo: smiling older man in a plaid shirt standing in a sunlit field"/>
    <ellipse cx="190" cy="205" rx="22" ry="14" fill="var(--green)" role="img" aria-label="Green leaf decoration"/>
    <circle cx="230" cy="330" r="28" fill="var(--blue-soft)" opacity=".6"/>
    <circle cx="370" cy="300" r="48" fill="var(--paper)" stroke="var(--blue-pale)" stroke-width="3"/>
    <circle cx="560" cy="205" r="62" fill="var(--paper)"/>
    <circle cx="560" cy="205" r="57" fill="#9a8a6a" role="img" aria-label="Photo: older woman gardening with a pot of flowers"/>
    <circle cx="650" cy="215" r="100" fill="var(--paper)" stroke="var(--blue)" stroke-width="2"/>
    <circle cx="650" cy="215" r="94" fill="#c9b8a4" role="img" aria-label="Photo: smiling older couple embracing"/>
    <circle cx="610" cy="300" r="18" fill="var(--blue-pale)" opacity=".7"/>
  </svg>
  <div class="fold" style="left:246.67px"></div>
  <div class="fold" style="left:493.33px"></div>

  <div class="panel panel--left">
    <h2 class="heading abs" style="left:28px;top:54px;font-size:20px">Our Philosophy</h2>
    <div class="rule" style="left:28px;top:82px;width:190px"></div>
    <p class="body-copy abs" style="left:28px;top:90px;width:192px">You may believe there is nothing you can do to prevent or treat cognitive decline and Alzheimer's disease. Maybe the idea of a personalized plan to prevent or reverse Alzheimer's sounds like 'snake oil' or wishful thinking. Thought Harbor can show you reputable science has opened new doors and created an unprecedented opportunity to change your brain health.</p>
    <p class="quote abs" style="left:22px;top:448px;width:210px">hope to people who consistently hear, "There is nothing we can do. Alzheimer's is a fatal disease." NOT TRUE! We see people's lives change every day!!!!</p>
  </div>

  <div class="panel panel--middle">
    <h2 class="heading abs" style="left:24px;top:50px;font-size:15px;text-transform:uppercase;letter-spacing:.3px">Join the Brain<br><span style="color:var(--green)">Health Revolution!</span></h2>
    <div class="rule" style="left:24px;top:92px;width:200px;background:var(--green)"></div>
    <ul class="ticks abs" style="left:26px;top:104px;width:205px;font-size:10.5px;line-height:1.35">
      <li style="margin-bottom:4px">Enhance Brain Function</li>
      <li style="margin-bottom:4px">Do not settle – Optimize your Brain at any age</li>
      <li style="margin-bottom:4px">Prevent Cognitive Decline</li>
      <li style="margin-bottom:4px">Reverse Early Dementia</li>
      <li>Proven strategies can change your life and destiny</li>
    </ul>
    <div class="brand-name abs" style="left:83px;top:285px;width:80px;text-align:center;font-size:11px;line-height:1.1">Thought Harbor</div>
    <p class="serif abs" style="left:0;width:246px;top:366px;text-align:center;color:var(--white);font-style:italic;font-size:12px">Call Us Now For Your</p>
    <p class="geo abs" style="left:0;width:246px;top:384px;text-align:center;color:var(--white);font-weight:700;font-size:15px">FREE CONSULTATION</p>
    <div class="pill" style="left:38px;top:408px;width:170px;height:26px;font-size:15px">
      <svg width="18" height="18" viewBox="0 0 18 18"><circle cx="9" cy="9" r="8" fill="none" stroke="var(--green)" stroke-width="2"/><path d="M6 5.5l1.5-.5 1 2-1 .8c.4 1 1.2 1.8 2.2 2.2l.8-1 2 1-.5 1.5c-3 .3-6.3-3-6-6z" fill="var(--green)"/></svg>
      555-014-2760
    </div>
    <p class="geo abs" style="left:0;width:246px;top:450px;text-align:center;color:var(--white);font-weight:700;font-size:13px">Contact Info</p>
    <div class="rule" style="left:48px;top:470px;width:150px;background:var(--white)"></div>
    <p class="contact-line abs" style="left:0;width:246px;top:480px">✉ info@thoughtharbor.com</p>
    <p class="contact-line abs" style="left:0;width:246px;top:497px">☏ 555-010-3344</p>
    <p class="contact-line abs" style="left:0;width:246px;top:514px">◍ www.thoughtharbor.org</p>
  </div>

  <div class="panel panel--right">
    <div class="abs" style="left:0;width:246px;top:40px;display:flex;flex-direction:column;align-items:center;gap:8px">
      <svg width="40" height="40" viewBox="0 0 40 40"><circle cx="20" cy="20" r="18" fill="none" stroke="var(--blue-deep)" stroke-width="2.5"/></svg>
      <div class="brand-name" style="font-size:19px">Thought Harbor</div>
    </div>
    <p class="serif abs" style="left:0;width:246px;top:410px;text-align:center;color:var(--white);font-weight:600;font-size:15px">You Can Change</p>
    <p class="serif abs" style="left:0;width:246px;top:430px;text-align:center;color:var(--white);font-weight:700;font-size:22px">Your Brain Health</p>
    <div class="pill" style="left:30px;top:466px;width:186px;height:22px;font-size:11px;font-weight:500">
      <svg width="10" height="10" viewBox="0 0 10 10"><circle cx="5" cy="5" r="5" fill="var(--green)"/></svg>
      www.thoughtharbor.org
    </div>
  </div>
</section>

<!-- Inside spread -->
<section class="spread spread--inside">
  <svg class="spread-art" width="740" height="572" viewBox="0 0 740 572">
    <defs>
      <linearGradient id="sky-field" x1="0" y1="0" x2="0" y2="1">
        <stop offset="0" stop-color="#5f9bd8"/>
        <stop offset=".3" stop-color="#cfe2f4"/>
        <stop offset=".62" stop-color="#e9f1f8"/>
        <stop offset=".72" stop-color="#8fae6a"/>
        <stop offset="1" stop-color="#3f6a22"/>
      </linearGradient>
    </defs>
    <rect width="740" height="572" fill="url(#sky-field)" role="img" aria-label="Photo: open wheat field under a bright blue sky at sunrise"/>
    <circle cx="370" cy="330" r="102" fill="var(--paper)" stroke="var(--blue)" stroke-width="2"/>
    <circle cx="370" cy="330" r="94" fill="#b59a72" role="img" aria-label="Photo: grandparents with a young granddaughter outdoors"/>
    <ellipse cx="405" cy="225" rx="26" ry="15" fill="var(--green)" role="img" aria-label="Green leaf decoration"/>
  </svg>
  <div class="fold" style="left:246.67px"></div>
  <div class="fold" style="left:493.33px"></div>

  <div class="panel panel--left">
    <h2 class="heading abs" style="left:26px;top:40px;font-size:19px;color:var(--ink)">Taking Care of<br>Your brain should not<br>Be a mystery</h2>
    <div class="rule" style="left:26px;top:112px;width:200px"></div>
    <div class="banner" style="left:28px;top:124px">HAVE YOU NOTICED?</div>
    <ul class="ticks abs" style="left:30px;top:160px;width:205px;font-size:10.5px;line-height:1.3;font-weight:500">
      <li style="margin-bottom:5px">Brain Fog</li>
      <li style="margin-bottom:5px">Lack of Mental Crispness</li>
      <li style="margin-bottom:5px">Difficulty Retrieving Common Information</li>
      <li style="margin-bottom:5px">Struggles Finding the Right Word</li>
      <li style="margin-bottom:5px">Family or Friends say, "I already told you that"</li>
      <li style="margin-bottom:5px">Changes in Your Mood</li>
      <li style="margin-bottom:5px">Your Physician Telling You There's Nothing That Can Be Done</li>
      <li style="margin-bottom:5px">Increasing Loneliness</li>
      <li>Not Knowing How to Help a Loved One with Dementia</li>
    </ul>
    <p class="serif abs" style="left:26px;top:410px;width:210px;color:var(--blue);font-style:italic;font-weight:700;font-size:14px;line-height:1.2">Cognitive decline is not inevitable or normal aging!</p>
  </div>

  <div class="panel panel--middle">
    <h2 class="heading abs" style="left:28px;top:40px;font-size:24px;color:var(--ink)">Our Services</h2>
    <div class="rule" style="left:28px;top:76px;width:190px"></div>
    <ul class="services abs" style="left:32px;top:86px">
      <li>Personal Services</li>
      <li>Remote Services</li>
      <li>Business Services</li>
      <li>Brain Studio</li>
    </ul>
  </div>

  <div class="panel panel--right">
    <h2 class="heading abs" style="left:22px;top:34px;font-size:18px;color:var(--ink)">Your Brain<br>Health Headquarters</h2>
    <div class="rule" style="left:22px;top:80px;width:205px"></div>
    <div class="abs" style="left:22px;top:88px;width:205px">
      <p class="body-copy" style="font-size:8.2px;margin-bottom:6px">Thought Harbor is your brain headquarters. We are a resource you can turn to for the latest tools, therapeutic devices, guidance, programs and insight necessary to protect and enhance your most important asset: YOUR BRAIN.</p>
      <p class="body-copy" style="font-size:8.2px;margin-bottom:6px">Thought Harbor has partnered with Clear Season Labs located in Riverton, Oregon. All labs are reviewed, and the Renew Protocol® is collaboratively developed and reviewed by Clear Season Labs. Their expertise and ongoing research bring another layer of assurance and confidence to the process.</p>
      <p class="body-copy" style="font-size:8.2px;margin-bottom:6px">According to the Memory Care Alliance, there are currently 6.2 million Americans living with Alzheimer's disease. That number is on target to triple between 2050 and 2060.</p>
      <p class="body-copy" style="font-size:8.2px;margin-bottom:6px">By the time a person reaches 65 years of age, 2 out of 9 have Alzheimer's. In fact, latest research indicates that well over 10 years before the first symptoms appear (as Mild Cognitive Impairment) the disease is already at work in the brain. By the time a person reaches 85 over 32% will have Alzheimer's and that number is increasing.</p>
      <p class="body-copy" style="font-size:8.2px">Present medications only manage symptoms or reduce existing Amyloid Plaque. New medications can cost as much as $52,000 a year, must be administered by IV and require monitoring through brain scans. The prevailing understanding has been that there is no cure, and Alzheimer's takes no hostages. All die!</p>
    </div>
  </div>
</section>

</body>
</html>
```